Business Card Design Project

Please create a custom business card for 'Journeys beyond the lantern'. The logo is attached to this brief.

Here is the link to the logo project : http://tasks.pixelmarrow.net/task.aspx?id=392017

Questions can be posted on the Discussion Board.

```html
<!DOCTYPE html>
<html lang="en">
<head>
<meta charset="utf-8">
<title>Nolvik business card</title>
<link rel="stylesheet" href="https://fonts.googleapis.com/css2?family=Open+Sans:wght@400;600;700&display=swap">
<style>
  :root {
    --brand-red: #ee2a24;
    --brand-red-deep: #c81f24;
    --ink: #1f1f1f;
    --ink-soft: #3a3a3a;
    --paper: #ffffff;
    --backdrop: #e9eaec;
  }
  * { box-sizing: border-box; margin: 0; padding: 0; }
  html, body { width: 1200px; height: 873px; overflow: hidden; }
  body {
    background: var(--backdrop);
    font-family: "Open Sans", Arial, sans-serif;
    display: flex;
    align-items: center;
    justify-content: center;
    gap: 40px;
  }
  .card {
    width: 540px;
    height: 310px;
    position: relative;
    box-shadow: 0 6px 18px rgba(0,0,0,0.18);
  }

  /* Front: white */
  .card-front { background: var(--paper); color: var(--ink); padding: 46px 44px; }
  .front-brand { display: flex; align-items: center; gap: 12px; }
  .front-brand .mark { width: 34px; height: 34px; background: var(--brand-red); }
  .front-brand .brand-name { font-weight: 600; font-size: 28px; color: var(--brand-red); letter-spacing: 0.5px; }
  .holder { margin-top: 26px; font-size: 21px; text-transform: uppercase; letter-spacing: 0.3px; }
  .holder .first { font-weight: 700; }
  .holder .divider { margin: 0 4px; color: var(--ink-soft); }
  .address { margin-top: 4px; font-size: 14px; color: var(--ink-soft); }
  .website { margin-top: 30px; font-size: 20px; letter-spacing: 0.8px; }

  /* Back: red */
  .card-back { background: var(--brand-red); color: var(--paper); padding: 40px 36px; }
  .contacts { list-style: none; display: flex; flex-direction: column; gap: 22px; }
  .contacts li { display: flex; align-items: center; gap: 10px; font-size: 15px; }
  .contacts .badge {
    width: 20px; height: 20px; border: 1.5px solid var(--paper); border-radius: 50%;
    display: flex; align-items: center; justify-content: center; font-size: 11px;
  }
  .back-brand {
    position: absolute; right: 36px; bottom: 34px;
    font-weight: 600; font-size: 84px; line-height: 1; letter-spacing: 1px;
  }
</style>
</head>
<body>
  <section class="card card-front">
    <div class="front-brand">
      <span class="mark"></span>
      <span class="brand-name">Nolvik</span>
    </div>
    <p class="holder"><span class="first">Dilan</span> Moraes<span class="divider">|</span>President</p>
    <p class="address">418/7 C, Kelanipura, Veyangoda Sri Lanka</p>
    <p class="website">www.nolvikstudio.com</p>
  </section>

  <section class="card card-back">
    <ul class="contacts">
      <li><span class="badge">T</span>0987654321</li>
      <li><span class="badge">F</span>0987654321</li>
      <li><span class="badge">E</span>hello@nolvikmail.com</li>
    </ul>
    <div class="back-brand">nolvik</div>
  </section>
</body>
</html>
```